R&T Night club Presents :

I need a advertiser 4 nights in one poster, from Thursday to Sunday,
Thursday : Every Thursday Irish Night
Friday: Old School Hip Hop, top 40 & request
Sat: Comet Saturdays July 11, July 25, August 8, August 22
Brazilian Night Forro: July 18, August 1, August 15 & August 29
Sunday: Velvet Sundaze ( Dj Marlow & Dj Vobo

Target Market(s)

All 4 Nights

Industry/Entity Type

School

Font styles to use
Decorative
Script

Requirements
Must have
• Poster 11x16 and talk about all 4 nights on, see up there description
Nice to have
• A lot of colors
Should not have
• Address: 812 Kelberry Rd Hyannis MA
• 5087162043
• Starting 9:30pm until 1:00Am
• 21+ ID
• Special Drinks $3.99

```html
<!DOCTYPE html>
<html lang="en">
<head>
<meta charset="utf-8">
<title>R&amp;T Night Club Presents</title>
<link rel="stylesheet" href="https://fonts.googleapis.com/css2?family=Orbitron:wght@500&family=Questrial&display=swap">
<style>
  :root {
    --night-deep: #0b0a3a;
    --white: #ffffff;
    --yellow: #ece41c;
    --lime: #b7d531;
    --green: #7cc242;
    --orange: #f8a51c;
    --coral: #f2683a;
    --label-green: #8cc63f;
  }
  html, body {
    margin: 0;
    padding: 0;
    overflow: hidden;
    background: var(--night-deep);
  }
  h1, h2, p { margin: 0; }
  .poster {
    position: relative;
    width: 820px;
    height: 1200px;
    overflow: hidden;
    font-family: "Questrial", "Century Gothic", sans-serif;
    color: var(--white);
    text-align: center;
  }
  .backdrop {
    position: absolute;
    inset: 0;
    width: 820px;
    height: 1200px;
  }
  .line {
    position: absolute;
    left: 0;
    width: 100%;
    line-height: 1;
    white-space: nowrap;
  }
  .brand-name {
    top: 175px;
    font-family: "Orbitron", sans-serif;
    font-weight: 500;
    font-size: 170px;
    letter-spacing: 6px;
    color: var(--lime);
  }
  .brand-type {
    top: 400px;
    font-size: 60px;
    letter-spacing: 1px;
  }
  .brand-presents {
    top: 464px;
    font-size: 32px;
  }
  .day-label {
    font-size: 22px;
    color: var(--label-green);
  }
  .day-label .dots {
    letter-spacing: 2px;
    font-size: 14px;
    vertical-align: middle;
    margin: 0 6px;
  }
  .day-thursday { top: 556px; }
  .day-friday { top: 689px; }
  .day-saturday { top: 802px; }
  .day-sunday { top: 1021px; }
  .event-title {
    font-family: "Orbitron", sans-serif;
    font-weight: 500;
    font-size: 26px;
    letter-spacing: 1px;
    text-transform: uppercase;
    -webkit-background-clip: text;
    background-clip: text;
    color: transparent;
  }
  .event-irish {
    top: 592px;
    background-image: linear-gradient(90deg, var(--yellow) 0%, var(--lime) 55%, var(--green) 100%);
  }
  .event-hiphop {
    top: 724px;
    background-image: linear-gradient(90deg, var(--orange) 0%, var(--yellow) 50%, var(--lime) 100%);
  }
  .event-sunday {
    top: 1060px;
    background-image: linear-gradient(90deg, var(--orange), var(--yellow));
  }
  .saturday-event {
    position: absolute;
    top: 842px;
    width: 360px;
  }
  .saturday-event.comet { left: 32px; }
  .saturday-event.forro { left: 429px; }
  .saturday-event .event-title {
    display: block;
    line-height: 40px;
  }
  .comet .event-title { background-image: linear-gradient(90deg, var(--orange), var(--yellow)); }
  .forro .event-title { background-image: linear-gradient(90deg, var(--lime), var(--green)); }
  .event-dates {
    margin-top: 4px;
    font-size: 22px;
    line-height: 36px;
  }
  .comet .event-dates { color: var(--coral); }
  .forro .event-dates { color: var(--label-green); }
  .event-djs {
    top: 1102px;
    font-size: 20px;
    color: var(--orange);
  }
</style>
</head>
<body>
<main class="poster">
  <svg class="backdrop" viewBox="0 0 820 1200" role="img" aria-label="Abstract night-club backdrop of purple light rays and soft blue bokeh glow">
    <defs>
      <radialGradient id="base-glow" cx="50%" cy="45%" r="75%">
        <stop offset="0%" stop-color="#2a27a0"/>
        <stop offset="55%" stop-color="#15125e"/>
        <stop offset="100%" stop-color="#08072e"/>
      </radialGradient>
      <radialGradient id="top-glow" cx="50%" cy="0%" r="60%">
        <stop offset="0%" stop-color="#c0398f" stop-opacity="0.75"/>
        <stop offset="50%" stop-color="#5a1a8a" stop-opacity="0.5"/>
        <stop offset="100%" stop-color="#5a1a8a" stop-opacity="0"/>
      </radialGradient>
      <radialGradient id="floor-glow" cx="50%" cy="100%" r="55%">
        <stop offset="0%" stop-color="#4b63e6" stop-opacity="0.7"/>
        <stop offset="100%" stop-color="#3d4fd0" stop-opacity="0"/>
      </radialGradient>
    </defs>
    <rect width="820" height="1200" fill="url(#base-glow)"/>
    <rect width="820" height="700" fill="url(#top-glow)"/>
    <rect y="750" width="820" height="450" fill="url(#floor-glow)"/>
  </svg>

  <h1 class="line brand-name">R&amp;T</h1>
  <p class="line brand-type">NIGHT CLUB</p>
  <p class="line brand-presents">PRESENTS</p>

  <p class="line day-label day-thursday"><span class="dots">••••</span>Thursday<span class="dots">••••</span></p>
  <h2 class="line event-title event-irish">Every Thursday Irish Night</h2>

  <p class="line day-label day-friday"><span class="dots">••••</span>Friday<span class="dots">••••</span></p>
  <h2 class="line event-title event-hiphop">Old School Hip Hop (Top 40 &amp; Request)</h2>

  <p class="line day-label day-saturday"><span class="dots">•••••••</span>Saturday<span class="dots">•••••••</span></p>
  <section class="saturday-event comet">
    <h2 class="event-title">Comet<br>Saturdays</h2>
    <p class="event-dates">July 11, 25,<br>August 8, 22</p>
  </section>
  <section class="saturday-event forro">
    <h2 class="event-title">Brazilian<br>Night Forro</h2>
    <p class="event-dates">July 18,<br>August 1, 15 &amp; 29</p>
  </section>

  <p class="line day-label day-sunday"><span class="dots">••••</span>Sunday<span class="dots">••••</span></p>
  <h2 class="line event-title event-sunday">Velvet Sundaze</h2>
  <p class="line event-djs">( Dj Marlow &amp; Dj Vobo )</p>
</main>
</body>
</html>
```